HLD business cards Dr. Martin Voss

I need a business card designed for our dental office. We are a "general dental" practice.
Looking for a clean, professional but not too fancy design with our logo and contact information required.
front of card is information/standard business card, backside is appt reminder with lines for date and time of appt
doctors name: Dr. Martin Voss DMD
office name: Voss Family Dental
address: 4827 N Birchwell Ave Palm Hollow, FL 33418
phone: 954-555-0173
Contact Information for Business Card
Office name, Doctor name, address, phone number...etc
- White/off white base color, blue and or black lettering

```html
<!DOCTYPE html>
<html lang="en">
<head>
<meta charset="utf-8">
<title>Voss Family Dental — Business Card</title>
<link rel="stylesheet" href="https://fonts.googleapis.com/css2?family=Montserrat:wght@300;400;500;700&family=Oswald:wght@600&display=swap">
<style>
  :root {
    --backdrop: #a9adae;
    --card: #f4f4f1;
    --ink: #141414;
    --muted: #6d6d6d;
    --rule: #3a3a3a;
    --dots: #555555;
  }
  * { box-sizing: border-box; margin: 0; padding: 0; }
  html, body { width: 1200px; height: 824px; overflow: hidden; }
  body {
    background: var(--backdrop);
    font-family: "Montserrat", sans-serif;
    color: var(--ink);
    display: flex;
    align-items: center;
    justify-content: center;
    gap: 40px;
  }
  .card {
    width: 540px;
    height: 310px;
    background: var(--card);
    box-shadow: 0 6px 18px rgba(0,0,0,0.18);
    position: relative;
  }

  /* Front */
  .card-front { display: flex; align-items: center; }
  .brand {
    width: 250px;
    display: flex;
    flex-direction: column;
    align-items: center;
    gap: 12px;
  }
  .brand-mark {
    width: 46px; height: 46px;
    border-radius: 50%;
    background: var(--ink);
  }
  .brand-name {
    font-family: "Montserrat", sans-serif;
    font-weight: 500;
    font-size: 19px;
    letter-spacing: 1.5px;
    text-transform: uppercase;
    color: var(--ink);
    text-align: center;
    line-height: 1.3;
  }
  .divider {
    width: 1px;
    height: 200px;
    background: var(--rule);
  }
  .contact { padding-left: 26px; }
  .doctor-name {
    font-family: "Oswald", sans-serif;
    font-weight: 600;
    font-size: 25px;
    text-transform: uppercase;
    letter-spacing: 0.5px;
    margin-bottom: 16px;
  }
  .contact-list { list-style: none; }
  .contact-item {
    display: flex;
    align-items: flex-start;
    gap: 9px;
    font-weight: 300;
    font-size: 15px;
    color: var(--muted);
    line-height: 1.35;
    margin-bottom: 4px;
  }
  .contact-icon { width: 13px; height: 13px; margin-top: 3px; flex: none; }

  /* Back */
  .card-back { padding: 26px 30px; font-size: 13px; }
  .appt-title {
    font-weight: 700;
    font-size: 17px;
    text-align: center;
    margin-bottom: 14px;
  }
  .field { display: flex; align-items: flex-end; gap: 8px; margin-bottom: 14px; }
  .field-label { font-weight: 500; white-space: nowrap; }
  .field-line { flex: 1; border-bottom: 1.5px dotted var(--dots); height: 12px; }
  .field-suffix { font-size: 11px; font-weight: 500; }
  .days { display: flex; justify-content: space-between; margin-bottom: 14px; }
  .day { display: flex; align-items: center; gap: 3px; font-size: 12px; font-weight: 500; }
  .day-box { width: 12px; height: 11px; border: 1.2px solid var(--ink); background: #fff; }
  .footnote {
    margin-top: 8px;
    font-size: 10px;
    text-align: center;
    color: var(--ink);
  }
</style>
</head>
<body>

  <section class="card card-front">
    <div class="brand">
      <div class="brand-mark"></div>
      <div class="brand-name">Voss Family<br>Dental</div>
    </div>
    <div class="divider"></div>
    <div class="contact">
      <h1 class="doctor-name">Dr. Martin Voss DMD</h1>
      <ul class="contact-list">
        <li class="contact-item">
          <svg class="contact-icon" viewBox="0 0 12 12"><path d="M6 0.5a4 4 0 0 0-4 4c0 3 4 7 4 7s4-4 4-7a4 4 0 0 0-4-4zm0 5.6a1.6 1.6 0 1 1 0-3.2 1.6 1.6 0 0 1 0 3.2z" fill="#141414"/></svg>
          <span>4827 N Birchwell Ave<br>Palm Hollow, FL 33418</span>
        </li>
        <li class="contact-item">
          <svg class="contact-icon" viewBox="0 0 12 12"><path d="M2.6 0.8l1.8 0 0.8 2.6-1.2 1c0.7 1.5 1.8 2.6 3.3 3.3l1-1.2 2.6 0.8 0 1.8c0 0.6-0.5 1.1-1.1 1.1C5.3 10.2 1.5 6.4 1.5 1.9c0-0.6 0.5-1.1 1.1-1.1z" fill="#141414"/></svg>
          <span>954-555-0173</span>
        </li>
        <li class="contact-item">
          <svg class="contact-icon" viewBox="0 0 12 12"><circle cx="6" cy="6" r="5.2" fill="#141414"/><circle cx="6" cy="6" r="2" fill="#f4f4f1"/></svg>
          <span>vossfamilydentalfl.com</span>
        </li>
      </ul>
    </div>
  </section>

  <section class="card card-back">
    <h2 class="appt-title">Next Appointment</h2>
    <div class="field"><span class="field-label">Name :</span><span class="field-line"></span></div>
    <div class="field"><span class="field-label">Date :</span><span class="field-line"></span></div>
    <div class="days">
      <span class="day">Sun<span class="day-box"></span></span>
      <span class="day">Mon<span class="day-box"></span></span>
      <span class="day">Tue<span class="day-box"></span></span>
      <span class="day">Wed<span class="day-box"></span></span>
      <span class="day">Thu<span class="day-box"></span></span>
      <span class="day">Fri<span class="day-box"></span></span>
      <span class="day">Sat<span class="day-box"></span></span>
    </div>
    <div class="field"><span class="field-label">Time :</span><span class="field-line"></span><span class="field-suffix">AM/PM</span></div>
    <div class="field"><span class="field-label">Note :</span><span class="field-line"></span></div>
    <div class="field"><span class="field-line"></span></div>
    <p class="footnote">Please call 24 hours ahead if you cannot keep your appointment or need it changed.</p>
  </section>

</body>
</html>
```